The WILLOW Lodge is a transitional living housue for women in recovery. It is structured and loving an

I have uploaded my old brochure which was not designed professionally. I want a fresh, funky feel. Our website is www.willowlodgeofthebrightcoast.example if you want to get ideas from that but I do not like the bubbles on it. I have uploded a few pics of the houses and the backyards. Please help us convey love and hope and recovery!

Industry/Entity Type

House

```html
<!DOCTYPE html>
<html lang="en">
<head>
<meta charset="utf-8">
<title>The WILLOW Lodge – Living in Recovery</title>
<link rel="stylesheet" href="https://fonts.googleapis.com/css2?family=Libre+Baskerville:ital@0;1&family=Didact+Gothic&display=swap">
<style>
  :root {
    --backdrop: #6f7072;
    --lilac-deep: #7d78a8;
    --lilac: #a29dc6;
    --lilac-pale: #bcb8d9;
    --leaf: #7f9a7a;
    --garden-dark: #3f5640;
    --garden: #6d8a63;
    --pool: #4fa7c4;
    --pool-light: #8fd0e0;
    --heading-purple: #4a3f7a;
    --heading-green: #c4e887;
    --text-light: #f7f6fb;
    --badge-purple: #5b2e8e;
    --badge-cyan: #6fd6dd;
  }
  html, body {
    margin: 0;
    width: 1200px;
    height: 900px;
    overflow: hidden;
    background: var(--backdrop);
  }
  .brochure {
    position: absolute;
    left: 60px;
    top: 32px;
    width: 1080px;
    height: 836px;
    display: flex;
    box-shadow: 0 10px 30px rgba(0,0,0,.35);
  }
  .panel {
    position: relative;
    width: 360px;
    height: 836px;
    overflow: hidden;
  }
  .panel-photo {
    position: absolute;
    inset: 0;
  }
  .photo-lilies {
    background:
      radial-gradient(ellipse at 30% 70%, rgba(127,154,122,.45), transparent 55%),
      radial-gradient(ellipse at 75% 30%, rgba(127,154,122,.35), transparent 50%),
      linear-gradient(170deg, var(--lilac-pale), var(--lilac) 45%, var(--lilac-deep));
  }
  .photo-garden {
    background:
      radial-gradient(ellipse at 50% 40%, rgba(150,175,140,.5), transparent 60%),
      linear-gradient(180deg, var(--garden), var(--garden-dark));
  }
  .photo-pool {
    background:
      linear-gradient(180deg, rgba(109,138,99,.9) 0%, rgba(130,150,120,.8) 35%, rgba(160,175,160,.8) 50%, var(--pool-light) 62%, var(--pool) 85%, #3c8ea9 100%);
  }
  .panel-content {
    position: relative;
    padding: 36px 30px;
    color: var(--text-light);
    font-family: "Didact Gothic", sans-serif;
  }
  .panel-title {
    margin: 8px 0 22px;
    font-family: "Libre Baskerville", serif;
    font-style: italic;
    font-weight: 400;
    font-size: 25px;
    color: var(--heading-purple);
    letter-spacing: .5px;
  }
  .body-copy {
    margin: 0 0 20px;
    font-size: 14.5px;
    line-height: 1.85;
    letter-spacing: 1.1px;
  }
  .right-copy .body-copy {
    font-size: 13px;
    line-height: 1.7;
    margin-bottom: 12px;
  }
  .section-heading {
    margin: 14px 0 4px;
    font-family: "Libre Baskerville", serif;
    font-style: italic;
    font-weight: 400;
    font-size: 14px;
    color: var(--heading-green);
    letter-spacing: .5px;
  }
  .partner-badge {
    position: absolute;
    right: 28px;
    bottom: 64px;
    width: 96px;
    height: 118px;
    background: linear-gradient(180deg, var(--badge-purple) 0 58%, var(--badge-cyan) 58% 100%);
  }
  .divider {
    border: 0;
    border-top: 1px solid rgba(255,255,255,.6);
    width: 70%;
    margin: 20px 0 18px auto;
  }
  .contact {
    text-align: right;
    font-family: "Libre Baskerville", serif;
    font-size: 15px;
    letter-spacing: 2px;
    line-height: 1.7;
    margin: 0;
  }
  .contact-phone {
    display: block;
    margin-top: 8px;
  }
</style>
</head>
<body>
  <main class="brochure">
    <section class="panel panel-left">
      <div class="panel-photo photo-lilies" role="img" aria-label="Lily pads floating on a pond, tinted soft lilac"></div>
      <div class="panel-content">
        <h1 class="panel-title">Living in Recovery</h1>
        <p class="body-copy">The WILLOW Lodge was created to offer women a safe, loving and structured place to live while building a solid foundation in recovery, with a twelve-step program at the heart of the home.</p>
        <p class="body-copy">We encourage the women to incorporate the spiritual principles of the program into their daily lives. We teach the values of discipline, responsibility, honesty and self-esteem. We provide comfortable and aesthetically appealing homes of which the women are proud to be a part.</p>
      </div>
      <div class="partner-badge" role="img" aria-label="Partner badge"></div>
    </section>

    <section class="panel panel-middle">
      <div class="panel-photo photo-garden" role="img" aria-label="Leafy garden path beside the house"></div>
    </section>

    <section class="panel panel-right">
      <div class="panel-photo photo-pool" role="img" aria-label="Backyard swimming pool surrounded by palms and garden chairs"></div>
      <div class="panel-content right-copy">
        <h2 class="section-heading">Our Managers</h2>
        <p class="body-copy">Managers have thorough knowledge of social services in our area. Some women may be eligible for assistance.</p>
        <h2 class="section-heading">Property Managers</h2>
        <p class="body-copy">Property Managers are in recovery. They also have experience in many areas of addiction-related problems and address the issues with the appropriate people.</p>
        <h2 class="section-heading">Career Skill Set</h2>
        <p class="body-copy">We encourage the women with more clean time to take on a lead position of responsibility in the houses. It enables women to be accountable to one another and not just authority figures.</p>
        <h2 class="section-heading">Mind, Body &amp; Spirit</h2>
        <p class="body-copy">Living clean and sober is a process. We encourage healing on all levels.</p>
        <h2 class="section-heading">Your Responsibility</h2>
        <p class="body-copy">You are responsible for making a decision to stay clean and sober, packing a bag and moving in. We supply linens, towels, cleaning and paper products.</p>
        <hr class="divider">
        <p class="contact">WILLOW Lodge of the Bright Coast<span class="contact-phone">(555) 014-7720</span></p>
      </div>
    </section>
  </main>
</body>
</html>
```